Postcard Design Project

Education- charter school- elementary k-6th grades- performing arts integrated in to the core curriculum

Industry/Entity Type

School

```html
<!DOCTYPE html>
<html lang="en">
<head>
<meta charset="utf-8">
<title>Bright Path Arts Academy – Enrollment Postcard</title>
<link href="https://fonts.googleapis.com/css2?family=Nunito:wght@400;600;700;800&display=swap" rel="stylesheet">
<style>
  :root{
    --page:#ecebef;
    --card:#ffffff;
    --purple:#5f4a9e;
    --purple-text:#5a4a9a;
    --magenta:#b34fa8;
    --yellow:#ebe22f;
    --lavender:#ece6f4;
    --ink-light:#ffffff;
    --star:#e6d51f;
  }
  *{box-sizing:border-box;margin:0;padding:0}
  html,body{width:1200px;height:900px;overflow:hidden}
  body{background:var(--page);font-family:"Nunito",sans-serif;position:relative}

  .postcard{position:absolute;top:135px;width:420px;height:630px;background:var(--card);
    box-shadow:0 6px 18px rgba(0,0,0,.18);overflow:hidden}
  .postcard--front{left:150px}
  .postcard--back{left:630px;
    background:linear-gradient(160deg,#ffffff 0%,#f3eff8 45%,#e9e2f2 100%)}

  /* shared name mark */
  .school-mark{position:absolute;display:flex;align-items:center;gap:8px;
    font-weight:700;font-size:15px;color:var(--purple-text);line-height:1.15}
  .school-mark__dot{width:14px;height:14px;border-radius:50%;background:var(--purple);flex:none}

  /* front */
  .front__mark{left:22px;top:24px;width:190px}
  .front__kids{position:absolute;left:0;top:70px;width:300px;height:230px}
  .front__silhouettes{position:absolute;left:185px;top:95px;width:235px;height:200px}
  .front__enroll{position:absolute;left:0;top:300px;width:272px;height:235px;background:var(--purple);
    padding:40px 22px;color:var(--ink-light);font-weight:800;font-size:34px;line-height:1.12}
  .front__yellow{position:absolute;left:287px;top:310px;width:133px;height:110px;background:var(--yellow)}
  .front__contact{position:absolute;left:287px;top:432px;width:133px;height:198px;background:var(--magenta)}
  .front__contact-wide{position:absolute;left:0;top:547px;width:420px;height:83px;background:var(--magenta);
    padding:12px 22px;color:var(--ink-light)}
  .front__name{font-size:19px;font-weight:600;line-height:1.15}
  .front__addr{font-size:12px;font-weight:600;line-height:1.35;margin-top:4px}

  /* back */
  .back__mark{left:50%;transform:translateX(-50%);top:34px;white-space:nowrap}
  .back__body{position:absolute;left:34px;right:34px;top:92px;text-align:center;color:var(--purple-text);
    font-size:12.5px;line-height:1.55}
  .back__body p{background:rgba(236,230,244,.55);padding:4px 8px}
  .back__star{display:block;margin:8px auto;width:16px;height:16px}
  .back__address{position:absolute;left:34px;right:34px;bottom:38px;text-align:center;
    color:var(--purple-text);font-size:17px;line-height:1.35}
</style>
</head>
<body>

<section class="postcard postcard--front" aria-label="Postcard front">
  <div class="front__kids" role="img" aria-label="Photo collage of children jumping with joy"
       style="background:linear-gradient(135deg,#f6f4f8 0%,#f4e6c8 40%,#e9a7c6 70%,#c3b2de 100%)"></div>
  <div class="front__silhouettes" role="img" aria-label="Photo of children's silhouettes dancing against a sunset"
       style="background:linear-gradient(160deg,#f4d9c8 0%,#d98a6a 50%,#4a2e2a 100%)"></div>
  <div class="school-mark front__mark"><span class="school-mark__dot"></span>Bright Path Arts Academy</div>
  <div class="front__enroll">Now Enrolling<br>2016-17 for<br>Grades k-6th</div>
  <div class="front__yellow"></div>
  <div class="front__contact"></div>
  <div class="front__contact-wide">
    <div class="front__name">Bright Path Arts Academy</div>
    <div class="front__addr">820 Maple Grove Lane · Riverton, Ohio 43100 · Phone: (555) 014-2290</div>
  </div>
</section>

<section class="postcard postcard--back" aria-label="Postcard back">
  <div class="school-mark back__mark"><span class="school-mark__dot"></span>Bright Path Arts Academy</div>
  <div class="back__body">
    <p>Bright Path Arts Academy is the most innovative public elementary school program in Central Ohio through integration of the fine arts in all subjects.</p>
    <svg class="back__star" viewBox="0 0 24 24" aria-hidden="true"><polygon fill="var(--star)" points="12,2 15,9 22,9.5 16.5,14 18.5,21 12,17 5.5,21 7.5,14 2,9.5 9,9"/></svg>
    <p>All grade levels take visual arts, music, drama and dance.</p>
    <svg class="back__star" viewBox="0 0 24 24" aria-hidden="true"><polygon fill="var(--star)" points="12,2 15,9 22,9.5 16.5,14 18.5,21 12,17 5.5,21 7.5,14 2,9.5 9,9"/></svg>
    <p>Small class sizes with Highly Qualified teachers in the core subjects, beautiful facilities with a five acre campus for outdoor learning, and a dedicated staff committed to a positive learning environment are just a few reasons you will be amazed by this performing arts community school.</p>
    <svg class="back__star" viewBox="0 0 24 24" aria-hidden="true"><polygon fill="var(--star)" points="12,2 15,9 22,9.5 16.5,14 18.5,21 12,17 5.5,21 7.5,14 2,9.5 9,9"/></svg>
    <p>Breakfast and lunch are provided at no cost to you! All of this tuition free! Please contact us for a tour of our school.</p>
    <svg class="back__star" viewBox="0 0 24 24" aria-hidden="true"><polygon fill="var(--star)" points="12,2 15,9 22,9.5 16.5,14 18.5,21 12,17 5.5,21 7.5,14 2,9.5 9,9"/></svg>
    <p>Classes fill up quickly so call today to ensure your child's enrollment for the 2016-17 school year.</p>
  </div>
  <div class="back__address">820 Maple Grove Lane<br>Riverton, Ohio 43100<br>Phone: (555) 014-2290</div>
</section>

</body>
</html>
```